Business Card Design Project

Professional business cards for law firm - a rough example of what we are looking for is attached. The logo, colour and styling of the name are all new and dont need to be changed. We need layout for front and back. We are looking for some imaginative layout of info. We are a young vibrant firm and not too conservative and are not adverse to something quite different.
Updates

Thank you for all the submissions.  We have been blown away with the quality of your work.  Our management team will be meeting later in the week to make our decision.  Again, thanks for the fabulous work.

Industry/Entity Type

Conservative

Requirements
Must have
• Logo and name as in attached example (colour and font)
Should not have
• Scales of Justice

```html
<!DOCTYPE html>
<html lang="en">
<head>
<meta charset="utf-8">
<title>Marlow Reed Legal – Business Card</title>
<link rel="stylesheet" href="https://fonts.googleapis.com/css2?family=PT+Sans:ital,wght@0,400;0,700;1,700&display=swap">
<style>
  :root {
    --brand-green: #6aa533;
    --edge-green: #4f8f1f;
    --ink: #1a1a1a;
    --card-border: #b9b9b9;
    --ring-grey: #9aa0a6;
    --paper: #ffffff;
  }
  * { box-sizing: border-box; margin: 0; padding: 0; }
  html, body {
    width: 1200px; height: 367px; overflow: hidden;
    background: var(--paper);
    font-family: "PT Sans", "Myriad Pro", sans-serif;
    color: var(--ink);
  }
  .canvas { position: relative; width: 1200px; height: 367px; }

  .card {
    position: absolute; top: 1px; height: 365px;
    border: 1px solid var(--card-border);
    background: var(--paper);
    overflow: hidden;
  }
  .card--front { left: 1px; width: 626px; }
  .card--back { left: 633px; width: 565px; }

  .card--front .edge-wash {
    position: absolute; inset: 0;
    background: radial-gradient(ellipse 150px 260px at 0% 72%, var(--edge-green) 0%, rgba(106,165,51,0.55) 35%, rgba(255,255,255,0) 100%);
  }
  .card--back .edge-wash {
    position: absolute; inset: 0;
    background: radial-gradient(ellipse 140px 300px at 100% 55%, var(--edge-green) 0%, rgba(106,165,51,0.5) 38%, rgba(255,255,255,0) 100%);
  }

  .firm-name {
    position: absolute; left: 202px; top: 26px;
    color: var(--brand-green); font-weight: 700;
    text-align: center; line-height: 1;
  }
  .firm-name__main { display: block; font-size: 27px; }
  .firm-name__sub { display: block; font-size: 15px; letter-spacing: 2.5px; margin-top: 5px; }

  .practice-areas {
    position: absolute; left: 34px; top: 113px;
    list-style: none; font-size: 18px; line-height: 22.6px;
  }

  .solicitor { position: absolute; left: 247px; top: 111px; }
  .solicitor__name { font-size: 20px; font-weight: 400; }
  .solicitor__role { font-size: 14.5px; margin-top: 8px; padding-left: 84px; }

  .contact {
    position: absolute; left: 247px; top: 190px;
    font-style: normal; font-size: 14.5px; line-height: 20.9px;
  }

  .tagline {
    position: absolute; left: 203px; top: 331px;
    font-size: 10.5px; font-weight: 700; font-style: italic;
  }

  .back-mark {
    position: absolute; left: 0; right: 0; top: 0; bottom: 0;
    display: flex; align-items: center; justify-content: center; gap: 14px;
  }
  .back-mark__ring { width: 46px; height: 46px; }
  .back-mark__name {
    color: var(--brand-green); font-weight: 700; font-size: 24px;
  }
</style>
</head>
<body>
<main class="canvas">
  <section class="card card--front" aria-label="Card front">
    <div class="edge-wash" aria-hidden="true"></div>

    <h1 class="firm-name">
      <span class="firm-name__main">Marlow Reed</span>
      <span class="firm-name__sub">LEGAL</span>
    </h1>

    <ul class="practice-areas">
      <li>Criminal</li>
      <li>Debt Recovery</li>
      <li>Dividing Fences</li>
      <li>Family</li>
      <li>Financial Agreements</li>
      <li>Probate/Wills</li>
      <li>Restraining Orders</li>
      <li>Traffic</li>
    </ul>

    <div class="solicitor">
      <p class="solicitor__name">Clara Ashdown LLB BA</p>
      <p class="solicitor__role">Solicitor</p>
    </div>

    <address class="contact">
      5/42 Carrow Street, Ridgeford WA 6110<br>
      PO Box 317, Ridgeford WA 6990<br>
      T: 9555 0142, 6555 0187<br>
      F: 6555 0239<br>
      E: reception@marlowreedlegal.com.au
    </address>

    <p class="tagline">helping you find the way forward</p>
  </section>

  <section class="card card--back" aria-label="Card back">
    <div class="edge-wash" aria-hidden="true"></div>
    <div class="back-mark">
      <svg class="back-mark__ring" viewBox="0 0 46 46" aria-hidden="true">
        <circle cx="23" cy="23" r="20" fill="none" stroke="var(--ring-grey)" stroke-width="3"/>
      </svg>
      <span class="back-mark__name">Marlow Reed Legal</span>
    </div>
  </section>
</main>
</body>
</html>
```